New logo and wordpress design for Brightmoor-hub.org

We run a website that collates profiles/interviews of individuals who have completed a PhD and moved away from a traditional academix career path into something related. This is often related to the field they studied in, such as publishing, government policy, consulting, teaching and many other things. The website https://brightmoor-hub.org aims to give students and researchers ideas about what paths they can take their career on.

We would like to refresh our brand with a new website and logo. Our website is run through wordpress and hence we would need appropriate files and designs to accomodate this.
Our new logo should represent the idea of navigating a career path and exploring the unknown. Up until now it has been a compass in tones of purple and blue. We are happy to keep this motif but would need an updated, more representative logo. We are also happy to get some new ideas if the designer has something they think would fit.
The website itself should have fresh and clean look. We would like a banner at the top with clear links to the various parts of the site. The banner should stay consistent throughout the site.
We would like the main page to have a clean and simple look which places the focus on the profiles and their associated photos.
We would like pictographs to represent the different fields which our profiles fit into and would like to discuss with the winning designer what these would look like exactly. As a starting point we would like pictographs representing STEM (Science, Technology, Engineering, Mathematics) and SHAPE (Social Sciences, Humanities and Arts for People and the Economy).

We are really looking for something that is clean and professional but embodies our mission to represent all of the major industries which doctoral graduates can go on to work in. Those being, academia (universities), government, industry (private enterprise and companies), and third sector (Charities and think tanks etc.). Any design should cover all of these and not focus just on a big business or similar. It should also represent that we are not purely science focused, but all disciplines and are a broad church in that sense. We are open to various colour schemes and ideas but would like something that gives a professional but approachable feel, it should have elements of Oxford, but not suggest that we are only open to Calderwick University students or graduates.
Some sites that may be useful are:
https://kestrelguild.org/news-resources/projects/research-culture/ - talks about the different areas of employment we are trying to represent
https://www.famden-lv.ac.uk/ an oxford internal website that we like the presentation of.

Target Market(s)

Academic researchers with a PhD

Industry/Entity Type

Academic Careers

Colors
0054AA
0677BA
7BADD7
CADEEF
E8F1F8
00AB8E
00BBA5
67D7C9
C6EFE9
E9F9F6
FFF300
FFF600
FEFA6F
FFFEC7
FFFEE8
6B429C
8869AF
B7A5CE
E3DAEB
F3F0F8

Requirements
Must have
• A new logo
Should not have
• The existing logo

```html
<!DOCTYPE html>
<html lang="en">
<head>
<meta charset="utf-8">
<title>Brightmoor Hub – Explore your options beyond academia</title>
<link rel="stylesheet" href="https://fonts.googleapis.com/css2?family=Poppins:wght@400;500;600;700&family=Inter:wght@400;500;600;700&display=swap">
<style>
:root{
  --ink:#16162a;
  --body:#3c3c4e;
  --muted:#77778a;
  --brand:#3a23a0;
  --brand-deep:#231585;
  --brand-violet:#6b3fb0;
  --lavender:#ebe8fa;
  --lavender-soft:#f1effb;
  --card:#f6f6f9;
  --line:#d9d5ef;
  --white:#ffffff;
}
*{box-sizing:border-box;margin:0;padding:0}
html,body{width:1200px;height:4425px;overflow:hidden;background:var(--white)}
body{position:relative;font-family:"Inter",sans-serif;color:var(--body)}
.abs{position:absolute}
h1,h2,h3{font-family:"Poppins",sans-serif;color:var(--ink);font-weight:500}
.pill{display:inline-flex;align-items:center;gap:5px;border:1.5px solid var(--brand);color:var(--brand);border-radius:20px;font-size:10.5px;font-weight:500;padding:6px 16px;background:transparent}
.pill.solid{background:var(--brand);color:var(--white)}
.pill.light{border-color:#fff;color:#fff}
.pill.glass{background:rgba(255,255,255,.18);border-color:transparent;color:#fff}
.photo{border-radius:2px}

/* header + hero */
.hero-band{left:0;top:0;width:1200px;height:580px;background:var(--lavender)}
.brand-mark{display:flex;align-items:center;gap:10px}
.brand-mark .dot{width:38px;height:38px;border-radius:50%;background:var(--brand)}
.brand-mark .name{font-family:"Poppins",sans-serif;font-weight:700;color:var(--brand);font-size:15px;line-height:1.05;letter-spacing:.3px}
.site-header{left:110px;top:18px;width:990px;height:60px;display:flex;align-items:center;justify-content:space-between}
.main-nav{display:flex;align-items:center;gap:22px;font-size:10.5px;color:var(--ink)}
.main-nav .current{color:var(--brand);font-weight:600}
.hero-title{left:0;top:125px;width:1200px;text-align:center;font-size:38px}
.hero-lead{left:0;top:193px;width:1200px;text-align:center;font-size:17px;line-height:1.35;color:var(--ink)}
.hero-cta{left:0;top:268px;width:1200px;text-align:center}
.hero-photo{left:106px;top:362px;width:987px;height:428px;background:linear-gradient(120deg,#2f3a55 0%,#6f7fa0 30%,#e9ecf2 55%,#8fa6c6 80%,#3b4a6a 100%)}

/* profiles */
.section-title{left:0;width:1200px;text-align:center;font-size:28px}
.section-lead{left:0;width:1200px;text-align:center;font-size:13px;line-height:1.5;color:var(--body)}
.profile-card{width:251px;height:442px;background:var(--card)}
.profile-card .photo{height:217px;width:100%}
.profile-card .date{font-size:8.5px;color:var(--ink);padding:4px 0 0 40px}
.profile-card .body{padding:9px 18px 0}
.profile-card h3{font-family:"Inter",sans-serif;font-size:11.5px;font-weight:600;color:var(--brand);margin-bottom:6px}
.profile-card .role{font-size:10px;line-height:1.35;color:var(--ink);margin-bottom:12px}
.profile-card .meta{font-size:8.6px;line-height:1.95;color:var(--muted)}
.profile-card .meta b{font-weight:500;color:var(--muted)}
.profile-card .excerpt{margin-top:12px;font-size:9.3px;line-height:1.45;color:var(--ink);font-weight:500}
.profile-card .more{color:var(--brand)}

/* purple feature */
.feature-band{left:0;top:2036px;width:1200px;height:796px;background:linear-gradient(100deg,var(--brand-deep) 0%,#2e1a92 45%,var(--brand-violet) 100%)}
.feature-photo-a{left:0;top:2004px;width:343px;height:338px;background:linear-gradient(140deg,#c7d6e6 0%,#6b88a8 45%,#e9a24a 62%,#34455e 100%)}
.feature-photo-b{left:405px;top:2496px;width:795px;height:336px;background:linear-gradient(90deg,#8e7c68 0%,#d7cdbd 40%,#efe9df 65%,#b9a48a 100%)}
.feature-title{left:405px;top:2110px;width:560px;font-size:28px;line-height:1.3;color:#fff;font-weight:400}
.feature-copy{left:405px;top:2258px;width:760px;font-size:9.6px;line-height:1.85;color:#e6e2fb}
.feature-cta{left:405px;top:2434px}

/* get involved */
.audience-photo{width:322px;height:322px;border-radius:50%;border:1.5px solid var(--brand)}
.audience h2{font-family:"Poppins",sans-serif;font-size:28px;font-weight:600;color:var(--brand);margin-bottom:14px}
.audience p{font-size:12.5px;line-height:1.5;color:var(--body);margin-bottom:16px}
.connector{height:1.5px;background:var(--brand)}
.connector-dot{width:6px;height:6px;border-radius:50%;background:var(--brand)}

/* join banner */
.footer-band{left:0;top:3900px;width:1200px;height:525px;background:var(--lavender-soft)}
.join-banner{left:198px;top:3758px;width:801px;height:270px;background:linear-gradient(100deg,var(--brand-deep),var(--brand-violet));text-align:center;color:#fff;padding-top:70px}
.join-banner p{font-family:"Poppins",sans-serif;font-size:18.5px;line-height:1.45}
.join-banner strong{font-weight:600}

/* footer */
.footer-brand{left:198px;top:4075px;width:260px;text-align:center}
.footer-brand .dot{width:96px;height:96px;border-radius:50%;background:var(--brand);margin:0 auto 20px}
.footer-brand .name{font-family:"Poppins",sans-serif;font-weight:700;color:var(--brand);font-size:20px;letter-spacing:.4px}
.footer-col h4{font-family:"Poppins",sans-serif;font-weight:500;font-size:12px;color:var(--ink);margin-bottom:14px}
.footer-col li{list-style:none;font-size:9px;line-height:1.65;color:var(--ink)}
.newsletter p{font-size:9px;line-height:1.5;color:var(--ink);margin-bottom:16px}
.newsletter .field{width:168px;height:24px;border-radius:14px;background:#fff;font-size:8px;color:var(--muted);padding:7px 14px;margin-bottom:14px}
.feed{left:906px;top:4060px;width:184px;height:240px;background:#fff;border-radius:4px;box-shadow:0 2px 10px rgba(40,30,110,.12);padding:10px 14px}
.feed .head{font-size:9px;font-weight:600;color:var(--ink);margin-bottom:16px}
.feed .sq{width:16px;height:16px;background:var(--ink);border-radius:2px;margin-bottom:30px}
.feed h5{font-family:"Inter",sans-serif;font-size:14px;font-weight:700;color:var(--ink);line-height:1.2;margin-bottom:8px}
.feed .note{font-size:7.5px;color:var(--muted);line-height:1.4;margin-bottom:12px}
.feed .btn{display:inline-block;background:#1d9bf0;color:#fff;font-size:8px;font-weight:600;border-radius:12px;padding:5px 14px}
.feed .bar{position:absolute;right:5px;top:30px;width:4px;height:190px;background:#d7d7de;border-radius:2px}
.copyright{left:198px;top:4344px;font-size:8.5px;color:var(--ink)}
.social{top:4336px;width:24px;height:24px;border-radius:50%;border:1.5px solid var(--brand)}
</style>
</head>
<body>

<!-- header & hero -->
<div class="abs hero-band"></div>
<header class="abs site-header">
  <div class="brand-mark"><span class="dot"></span><span class="name">BRIGHTMOOR<br>HUB</span></div>
  <nav class="main-nav">
    <span class="current">Home</span><span>Career profiles</span><span>Get involved</span><span>Events</span><span>Resources</span><span>About us</span>
    <svg width="12" height="12" viewBox="0 0 12 12" aria-label="Search"><circle cx="5" cy="5" r="3.8" fill="none" stroke="#3a23a0" stroke-width="1.5"/><line x1="7.8" y1="7.8" x2="11" y2="11" stroke="#3a23a0" stroke-width="1.5"/></svg>
    <span class="pill solid">Contact us ↗</span>
  </nav>
</header>
<h1 class="abs hero-title">Explore your options beyond academia</h1>
<p class="abs hero-lead">A collection of profiles of people who have made the<br>transition from academia to industry.</p>
<div class="abs hero-cta"><span class="pill">Contact us ↗</span></div>
<div class="abs hero-photo photo" role="img" aria-label="Smiling researcher in a lab coat working at a microscope in a laboratory"></div>

<!-- career profiles -->
<h2 class="abs section-title" style="top:862px">Career profiles</h2>
<p class="abs section-lead" style="top:918px">Explore a collection of profiles from researchers pursuing<br>careers beyond academia.</p>

<article class="abs profile-card" style="left:198px;top:985px">
  <div class="photo" role="img" aria-label="Portrait of Marisol Ortega-Vance" style="background:linear-gradient(160deg,#9b8f86,#3a302c)"></div>
  <div class="date">June 12, 2024</div>
  <div class="body">
    <h3>Marisol Ortega-Vance</h3>
    <p class="role">Behavioural Scientist<br>at Lumenfield</p>
    <p class="meta">Career profiles: PhD<br>Degree: Psychology<br>Left academia after: 6+ Years postdoc<br>Sector: Charities</p>
    <p class="excerpt">My favorite parts of my job include developing behavioral solutions and running trials...<span class="more">[ more ]</span></p>
  </div>
</article>
<article class="abs profile-card" style="left:473px;top:985px">
  <div class="photo" role="img" aria-label="Portrait of Owen Hartley" style="background:linear-gradient(160deg,#d8c36a,#6f6d6a 45%,#2f2e33)"></div>
  <div class="date">May 21, 2024</div>
  <div class="body">
    <h3>Owen Hartley</h3>
    <p class="role">Student Engagement Manager<br>at Alder Materials Institute</p>
    <p class="meta">Career profiles: PhD<br>Degree: Material science<br>Left academia after: PhD<br>Sector: Higher Education</p>
    <p class="excerpt">My background is in Materials Science and Engineering, I studied for my BSc at The University of Ashbury...<span class="more">[ more ]</span></p>
  </div>
</article>
<article class="abs profile-card" style="left:750px;top:985px">
  <div class="photo" role="img" aria-label="Portrait of Anjali Varma by a lake" style="background:linear-gradient(160deg,#4a7fa8,#7a6a58 60%,#c9c2c6)"></div>
  <div class="date">April 2, 2024</div>
  <div class="body">
    <h3>Anjali Varma</h3>
    <p class="role">Consultant<br>at Independent/Freelance</p>
    <p class="meta">Career profiles: PhD<br>Degree: Biochemistry<br>Left academia after: 3-6 Years postdoc<br>Sector: Museums, Sustainable...</p>
    <p class="excerpt">I wanted to be a bridge between science and society, I wanted a better balance between scholarly and artistic...<span class="more">[ more ]</span></p>
  </div>
</article>

<article class="abs profile-card" style="left:198px;top:1456px">
  <div class="photo" role="img" aria-label="Portrait of Meera Kapoor" style="background:linear-gradient(160deg,#e8ddd6,#b48a80 55%,#6a4c4a)"></div>
  <div class="date">April 2, 2024</div>
  <div class="body">
    <h3>Meera Kapoor</h3>
    <p class="role">Visual Science Communicator<br>at Inkwell Studio</p>
    <p class="meta">Career profiles: PhD<br>Degree: Molecular biology<br>Left academia after: 0-3 Years postdoc<br>Sector: Freelance, Science...</p>
    <p class="excerpt">You can contribute to science even if you are not on the bench!...<span class="more">[ more ]</span></p>
  </div>
</article>
<article class="abs profile-card" style="left:473px;top:1456px">
  <div class="photo" role="img" aria-label="Portrait of Emre Aydan in an office corridor" style="background:linear-gradient(160deg,#8d939c,#4a4d55 55%,#1f2430)"></div>
  <div class="date">May 21, 2024</div>
  <div class="body">
    <h3>Emre Aydan</h3>
    <p class="role">Quality Engineer at Norvale Group<br>(Fenwick Medical GmbH)</p>
    <p class="meta">Career profiles: PhD<br>Degree: Biomedical engineering<br>Left academia after: PhD<br>Sector: Biomedical materials</p>
    <p class="excerpt">Helping the company in clarification of quality-critical questions with customers or the development team...<span class="more">[ more ]</span></p>
  </div>
</article>
<article class="abs profile-card" style="left:750px;top:1456px">
  <div class="photo" role="img" aria-label="Portrait of Layla Haddad" style="background:linear-gradient(160deg,#2d3c5c,#6a5a62 55%,#c6b8b8)"></div>
  <div class="date">February 20, 2024</div>
  <div class="body">
    <h3>Layla Haddad</h3>
    <p class="role">Assistant Director- Analytics &amp;<br>Modelling - Event Response...</p>
    <p class="meta">Career profiles: PhD<br>Degree: Biochemistry<br>Left academia after: 0-3 Years postdoc<br>Sector: Consulting</p>
    <p class="excerpt">Do informational interviews, they can be very helpful. Use your network to look for opportunities and learn about...<span class="more">[ more ]</span></p>
  </div>
</article>

<div class="abs" style="left:0;top:1936px;width:1200px;text-align:center"><span class="pill">View all profiles ↗</span></div>

<!-- feature band -->
<div class="abs feature-band"></div>
<div class="abs feature-photo-a" role="img" aria-label="Engineer in a hard hat against a bright industrial skyline"></div>
<h2 class="abs feature-title">Researchers find all sorts of rewarding careers – Smart people work everywhere!</h2>
<p class="abs feature-copy">Such diversity in potential roles can prove challenging when exploring your options.<br>This collection of career profiles enables you to see what others in your position chose to do, why and how they made the move, and what they most enjoy about their job. You will get a feel for their daily activities, workplace culture and work-life balance.Top tip: Look out for authors' insights into which skills developed during or after their PhD proved helpful in getting their job, and performing well there. You'll be encouraged to see how people are building on their research expertise to thrive in newer roles.And don't miss the "employer bio" at the end of each career profile for careers opportunities in each organisation.</p>
<div class="abs feature-cta"><span class="pill glass">Who we are ↗</span></div>
<div class="abs feature-photo-b" role="img" aria-label="Two colleagues talking across a desk with a laptop in a bright office"></div>

<!-- get involved -->
<h2 class="abs section-title" style="top:2905px;font-size:36px;font-weight:600">Get involved</h2>
<p class="abs section-lead" style="top:2962px;font-size:16px;line-height:1.4;color:var(--ink)">See how you can contribute to the Brightmoor Hub<br>Options beyond academia project.</p>

<div class="abs audience-photo" style="left:198px;top:3049px;background:linear-gradient(150deg,#e9e3d8,#a58d74 55%,#5a6e7c)" role="img" aria-label="Researcher smiling while working on a laptop"></div>
<div class="abs connector" style="left:530px;top:3211px;width:70px"></div>
<div class="abs connector-dot" style="left:597px;top:3208px"></div>
<div class="abs audience" style="left:781px;top:3130px;width:330px">
  <h2>Researchers</h2>
  <p>Are you a researcher keen to know more about roles beyond academia? And to extend your professional network?</p>
  <span class="pill">Find out more ↗</span>
</div>

<div class="abs audience-photo" style="left:667px;top:3369px;background:linear-gradient(150deg,#dfe3ea,#7d8796 50%,#2f3a4c)" role="img" aria-label="Group of colleagues gathered around a laptop in a meeting"></div>
<div class="abs connector" style="left:600px;top:3530px;width:66px"></div>
<div class="abs connector-dot" style="left:597px;top:3527px"></div>
<div class="abs audience" style="left:198px;top:3460px;width:330px">
  <h2>Employers</h2>
  <p>Do you want to raise your profile amongst researchers?</p>
  <span class="pill">Find out more ↗</span>
</div>

<!-- join banner & footer -->
<div class="abs footer-band"></div>
<div class="abs join-banner">
  <p><strong>If you're a Dphil student or member of research staff at the<br>Calderwick University,</strong> you can join the editorial team!<br>please contact us to find out more.</p>
  <div style="margin-top:24px"><span class="pill light">Contact us ↗</span></div>
</div>

<div class="abs footer-brand">
  <div class="dot"></div>
  <div class="name">BRIGHTMOOR HUB</div>
</div>
<div class="abs footer-col" style="left:447px;top:4112px">
  <h4>Quick links</h4>
  <ul><li>Home</li><li>Career profiles</li><li>Get involved</li><li>Events</li><li>Resources</li><li>About us</li><li>Contact us</li></ul>
</div>
<div class="abs footer-col newsletter" style="left:616px;top:4112px;width:200px">
  <h4>Join our newsletter</h4>
  <p>Keep up our latest news and events to<br>subscribe our newsletter</p>
  <div class="field">Enter your email...</div>
  <span class="pill solid">Submit ↗</span>
</div>
<aside class="abs feed">
  <div class="head">Posts from @BrightmoorPhD</div>
  <div class="sq"></div>
  <h5>Nothing to see<br>here - yet</h5>
  <p class="note">When they post, their posts will<br>show up here.</p>
  <span class="btn">View on it</span>
  <span class="bar"></span>
</aside>
<p class="abs copyright">© 2024 <strong>Brightmoor Hub</strong> - All rights reserved</p>
<span class="abs social" style="left:704px" aria-label="Social profile"></span>
<span class="abs social" style="left:740px" aria-label="Social profile"></span>

</body>
</html>
```